Local Roofing/Construction company business needs new biz card design

We need a new business card design, current cards are from the start of this operation and generic at best. We are a local Construction Company (General Contractor) with a majority of our work originating from insurance claims-exterior finish work is the main focus (Roofs-Siding-Gutters etc). Heavily involved with homeowners and the low ball offers they receive from insurance company's after a insurable event takes place. I have attached some of our original logo file(s) below.

```html
<!DOCTYPE html>
<html lang="en">
<head>
<meta charset="utf-8">
<title>Stonebridge Builders – Business Card</title>
<link href="https://fonts.googleapis.com/css2?family=Montserrat:wght@400;500;700;800&display=swap" rel="stylesheet">
<style>
  :root {
    --green: #58b56e;
    --ink: #0f2026;
    --text: #2b2b2b;
    --paper: #ffffff;
    --backdrop: #c9c9c9;
  }
  * { margin: 0; padding: 0; box-sizing: border-box; }
  html, body { width: 1200px; height: 802px; overflow: hidden; }
  body {
    background: var(--backdrop);
    font-family: "Montserrat", sans-serif;
    display: flex;
    align-items: center;
    justify-content: center;
    gap: 40px;
  }
  .card {
    position: relative;
    width: 540px;
    height: 309px;
    border-radius: 22px;
    overflow: hidden;
  }
  .card-front { background: var(--paper); color: var(--text); }
  .card-back {
    background: var(--green);
    display: flex;
    align-items: center;
    justify-content: center;
  }
  .brand {
    display: flex;
    align-items: center;
    gap: 10px;
    font-weight: 800;
    text-transform: uppercase;
    letter-spacing: 0.04em;
    line-height: 1.05;
  }
  .brand-mark { display: block; background: currentColor; }
  .card-front .brand {
    position: absolute;
    top: 36px;
    right: 34px;
    color: var(--green);
    font-size: 17px;
  }
  .card-front .brand-mark { width: 16px; height: 16px; }
  .card-back .brand { color: var(--ink); font-size: 34px; gap: 16px; }
  .card-back .brand-mark { width: 30px; height: 30px; }
  .accent {
    position: absolute;
    left: 0;
    top: 148px;
    width: 22px;
    height: 40px;
    background: var(--green);
  }
  .person { position: absolute; left: 44px; top: 144px; }
  .person-name {
    color: var(--green);
    font-weight: 700;
    font-size: 21px;
    letter-spacing: 0.05em;
    text-transform: uppercase;
  }
  .person-title { font-size: 13px; font-weight: 500; margin-top: 2px; }
  .divider {
    position: absolute;
    left: 44px;
    right: 34px;
    top: 200px;
    height: 1px;
    background: var(--green);
  }
  .contacts {
    position: absolute;
    left: 44px;
    top: 214px;
    list-style: none;
    font-size: 13px;
    line-height: 22px;
  }
  .contacts li { display: flex; align-items: center; gap: 8px; }
  .contacts svg { width: 11px; height: 11px; fill: var(--green); flex: none; }
  .address {
    position: absolute;
    right: 34px;
    top: 214px;
    text-align: right;
    font-size: 13px;
    line-height: 20px;
    font-style: normal;
  }
</style>
</head>
<body>
  <section class="card card-front" aria-label="Card front">
    <div class="brand"><span class="brand-mark"></span><span>Stonebridge<br>Builders</span></div>
    <span class="accent"></span>
    <div class="person">
      <p class="person-name">Colin Mercer</p>
      <p class="person-title">Managing Director</p>
    </div>
    <span class="divider"></span>
    <ul class="contacts">
      <li><svg viewBox="0 0 24 24"><path d="M6.6 10.8a15 15 0 0 0 6.6 6.6l2.2-2.2a1 1 0 0 1 1-.25 11.4 11.4 0 0 0 3.6.57 1 1 0 0 1 1 1V20a1 1 0 0 1-1 1A17 17 0 0 1 3 4a1 1 0 0 1 1-1h3.5a1 1 0 0 1 1 1c0 1.25.2 2.45.57 3.57a1 1 0 0 1-.25 1z"/></svg>0400 555 218</li>
      <li><svg viewBox="0 0 24 24"><path d="M2 5h20v14H2z M2 5l10 8 10-8" /></svg>info@stonebridgebuilders.com</li>
      <li><svg viewBox="0 0 24 24"><circle cx="12" cy="12" r="10"/></svg>www.stonebridgebuilders.com</li>
    </ul>
    <address class="address">418 Harlow Avenue<br>Ridgefield County 5230</address>
  </section>

  <section class="card card-back" aria-label="Card back">
    <div class="brand"><span class="brand-mark"></span><span>Stonebridge<br>Builders</span></div>
  </section>
</body>
</html>
```